Looking for a professional, clean and crisp business card

I am in the underground utilities industry and am just looking for a really impressive business card. I would like our card to be white with our symbol crisp and clear with it protruding. I also have a business partner that will require his name and info on the card once the design is set. I would like to have our website info on the card which is;
http://granitetrenchco.example/

Contact Information for Business Card

Website, contact name, number and email

```html
<!DOCTYPE html>
<html lang="en">
<head>
<meta charset="utf-8">
<title>Granite Trench Co – Business Card</title>
<link href="https://fonts.googleapis.com/css2?family=Montserrat:wght@400;500;600&display=swap" rel="stylesheet">
<style>
  :root {
    --page-bg: #f6f7f9;
    --card-white: #ffffff;
    --card-black: #000000;
    --ink: #222222;
    --muted: #6a6a6a;
    --icon: #8a8a8a;
    --accent-blue: #5b8ae0;
    --shadow: 0 18px 40px rgba(40, 50, 70, 0.14);
  }
  * { box-sizing: border-box; margin: 0; padding: 0; }
  html, body {
    width: 1030px; height: 1200px; overflow: hidden;
    background: var(--page-bg);
    font-family: "Montserrat", Arial, sans-serif;
  }
  .canvas {
    width: 1030px; height: 1200px;
    display: flex; flex-direction: column; align-items: center; justify-content: center;
    gap: 80px;
  }
  .card {
    width: 760px; height: 447px;
    box-shadow: var(--shadow);
    position: relative;
  }
  .card--front {
    background: var(--card-black);
    display: flex; align-items: center; justify-content: center;
  }
  .brand-mark {
    display: flex; align-items: center; gap: 14px;
    font-weight: 600; font-size: 30px; letter-spacing: 0.5px;
  }
  .brand-mark__dot {
    width: 22px; height: 22px; border-radius: 50%;
  }
  .card--front .brand-mark { color: #ffffff; }
  .card--front .brand-mark__dot { background: #ffffff; }

  .card--back { background: var(--card-white); }
  .card--back .brand-mark {
    position: absolute; left: 70px; top: 202px;
    color: var(--ink); font-size: 22px; gap: 10px;
  }
  .card--back .brand-mark__dot { background: var(--ink); width: 16px; height: 16px; }

  .contact {
    position: absolute; left: 387px; top: 112px; right: 0;
  }
  .contact__name {
    font-size: 38px; font-weight: 600; color: var(--ink); line-height: 1.05;
  }
  .contact__role {
    font-size: 18px; font-weight: 500; color: var(--ink); margin-top: 2px;
  }
  .contact__rule {
    height: 3px; background: var(--accent-blue); margin-top: 18px;
  }
  .contact__list { list-style: none; margin-top: 26px; }
  .contact__item {
    display: flex; align-items: flex-start; gap: 14px;
    font-size: 18px; color: var(--muted); line-height: 1.25;
    margin-bottom: 12px;
  }
  .contact__icon { width: 20px; height: 20px; flex: none; fill: var(--icon); margin-top: 1px; }
</style>
</head>
<body>
<main class="canvas">
  <section class="card card--front" aria-label="Card front">
    <div class="brand-mark"><span class="brand-mark__dot"></span>Granite Trench Co</div>
  </section>

  <section class="card card--back" aria-label="Card back">
    <div class="brand-mark"><span class="brand-mark__dot"></span>Granite Trench Co</div>
    <div class="contact">
      <h1 class="contact__name">Dale Morrow</h1>
      <p class="contact__role">Owner</p>
      <div class="contact__rule"></div>
      <ul class="contact__list">
        <li class="contact__item">
          <svg class="contact__icon" viewBox="0 0 24 24"><path d="M6.6 10.8a15.2 15.2 0 0 0 6.6 6.6l2.2-2.2a1 1 0 0 1 1-.25 11.4 11.4 0 0 0 3.6.57 1 1 0 0 1 1 1V20a1 1 0 0 1-1 1A17 17 0 0 1 3 4a1 1 0 0 1 1-1h3.5a1 1 0 0 1 1 1c0 1.25.2 2.45.57 3.6a1 1 0 0 1-.25 1z"/></svg>
          555-014-2290
        </li>
        <li class="contact__item">
          <svg class="contact__icon" viewBox="0 0 24 24"><path d="M3 5h18v14H3z M3 5l9 7 9-7" fill="var(--icon)" stroke="#fff" stroke-width="1.5"/></svg>
          Dale@granitetrenchco.example
        </li>
        <li class="contact__item">
          <svg class="contact__icon" viewBox="0 0 24 24"><circle cx="12" cy="12" r="9" fill="none" stroke="var(--icon)" stroke-width="2"/><path d="M3 12h18M12 3c3 3 3 15 0 18M12 3c-3 3-3 15 0 18" fill="none" stroke="var(--icon)" stroke-width="1.5"/></svg>
          granitetrenchco.example
        </li>
        <li class="contact__item">
          <svg class="contact__icon" viewBox="0 0 24 24"><path d="M12 2a7 7 0 0 0-7 7c0 5.2 7 13 7 13s7-7.8 7-13a7 7 0 0 0-7-7zm0 9.5A2.5 2.5 0 1 1 12 6.5a2.5 2.5 0 0 1 0 5z"/></svg>
          <span>Alder Bend, British Columbia,<br>Canada</span>
        </li>
      </ul>
    </div>
  </section>
</main>
</body>
</html>
```